Business cards and letterhead
cards and letterhead
Thanks all designers for your hard work.
Does anybody have anything different than just the swirl line through it?
I realy want the web address to stand out somehow, everybody just keep putting it in small letters...
Let's just leave off the email and make the web address stand out better.
creater I like #18 in black, the RT gets lost on the background. could it have a small white outline or something so it stands out. Website address must be on there, my email is not that important. Thanks
I like the color on there it makes it pop.
I want the web address to stand out. Thanks

```html
<!DOCTYPE html>
<html lang="en">
<head>
<meta charset="utf-8">
<title>RT Auto Sales – Business Cards</title>
<link href="https://fonts.googleapis.com/css2?family=Arimo:wght@400;700&family=Russo+One&display=swap" rel="stylesheet">
<style>
  :root {
    --page: #ffffff;
    --navy: #1e2a78;
    --royal: #2b3fb0;
    --red: #b3232d;
    --orange: #f0621c;
    --ink: #1a1a1a;
    --grey: #6b6b6b;
    --white: #ffffff;
    --black: #0c0c0c;
    --web-light: #ffd84a;
    --web-dark: #ff8a3d;
  }
  * { box-sizing: border-box; margin: 0; padding: 0; }
  html, body { width: 1200px; height: 734px; overflow: hidden; background: var(--page); }
  .sheet { position: relative; width: 1200px; height: 734px; }

  .card {
    position: absolute; width: 552px; height: 320px;
    border-radius: 16px; overflow: hidden;
    box-shadow: 0 2px 6px rgba(0,0,0,.25);
  }
  .card--light { background: var(--white); }
  .card--dark  { background: linear-gradient(160deg, #222 0%, var(--black) 60%); }
  .pos-tl { left: 30px;  top: 28px; }
  .pos-tr { left: 604px; top: 28px; }
  .pos-bl { left: 30px;  top: 376px; }
  .pos-br { left: 604px; top: 376px; }

  .swoosh { position: absolute; inset: 0; width: 100%; height: 100%; }

  .brand {
    position: absolute; font-family: "Russo One", sans-serif;
    font-weight: 400; font-size: 40px; line-height: 1; color: var(--navy);
    white-space: nowrap;
  }
  .card--dark .brand { color: var(--royal); }
  .brand--front { left: 30px; top: 44px; }
  .brand--back  { right: 34px; bottom: 40px; }

  .holder { position: absolute; left: 30px; top: 152px; font-family: "Arimo", sans-serif; }
  .holder__name { font-size: 28px; line-height: 32px; font-weight: 700; color: var(--ink); }
  .holder__role { font-size: 16px; line-height: 20px; color: var(--grey); margin-top: 2px; }
  .card--dark .holder__name { color: var(--white); }
  .card--dark .holder__role { color: #bdbdbd; }

  .contact {
    position: absolute; right: 18px; top: 190px; text-align: right;
    font-family: "Arimo", sans-serif; font-size: 13.5px; line-height: 17px;
    color: var(--white); list-style: none;
  }
  .contact__web {
    margin-top: 6px; font-size: 20px; line-height: 24px; font-weight: 700;
    color: var(--web-light); letter-spacing: .3px;
  }
  .card--dark .contact__web { color: var(--web-dark); }

  .vehicle-photo { position: absolute; left: 18px; top: 10px; width: 350px; height: 215px; border-radius: 40px 60px 30px 30px; }
  .card--light .vehicle-photo { background: radial-gradient(ellipse at 50% 55%, rgba(205,120,110,.35), rgba(230,200,195,.15) 70%, transparent 100%); }
  .card--dark .vehicle-photo { background: radial-gradient(ellipse at 50% 55%, rgba(120,95,85,.55), rgba(60,50,45,.25) 70%, transparent 100%); }
</style>
</head>
<body>
<main class="sheet">

  <!-- Light front -->
  <section class="card card--light pos-tl">
    <svg class="swoosh" viewBox="0 0 552 320" preserveAspectRatio="none" aria-hidden="true">
      <defs>
        <linearGradient id="blueFill" x1="0" y1="0" x2="1" y2="1">
          <stop offset="0" stop-color="#2b3fb0"/><stop offset="1" stop-color="#1a2366"/>
        </linearGradient>
      </defs>
      <path d="M0 226 C210 224 410 150 552 8 L552 44 C420 170 220 252 0 256 Z" fill="var(--red)"/>
      <path d="M0 266 C230 262 430 180 552 58 L552 320 L0 320 Z" fill="url(#blueFill)"/>
    </svg>
    <div class="brand brand--front">RT Auto Sales</div>
    <div class="holder">
      <p class="holder__name">Daniel Ward</p>
      <p class="holder__role">Owner</p>
    </div>
    <ul class="contact">
      <li>418 W. Harbor Ln.</li>
      <li>Lakeport, TX 77031</li>
      <li>Phone: 555-310-4821</li>
      <li>Fax: 555-310-4830</li>
      <li class="contact__web">rtautosales.biz</li>
    </ul>
  </section>

  <!-- Light back -->
  <section class="card card--light pos-tr">
    <div class="vehicle-photo" role="img" aria-label="Faded photo of a pickup truck"></div>
    <div class="brand brand--back">RT Auto Sales</div>
  </section>

  <!-- Dark front -->
  <section class="card card--dark pos-bl">
    <svg class="swoosh" viewBox="0 0 552 320" preserveAspectRatio="none" aria-hidden="true">
      <defs>
        <linearGradient id="blueFillDark" x1="0" y1="0" x2="1" y2="1">
          <stop offset="0" stop-color="#3550d0"/><stop offset="1" stop-color="#1a2366"/>
        </linearGradient>
      </defs>
      <path d="M0 226 C210 224 410 150 552 8 L552 44 C420 170 220 252 0 256 Z" fill="var(--royal)"/>
      <path d="M0 266 C230 262 430 180 552 58 L552 320 L0 320 Z" fill="url(#blueFillDark)"/>
      <path d="M0 266 C120 266 230 284 310 320 L250 320 C190 296 100 290 0 290 Z" fill="var(--orange)"/>
    </svg>
    <div class="brand brand--front">RT Auto Sales</div>
    <div class="holder">
      <p class="holder__name">Daniel Ward</p>
      <p class="holder__role">Owner</p>
    </div>
    <ul class="contact">
      <li>418 W. Harbor Ln.</li>
      <li>Lakeport, TX 77031</li>
      <li>Phone: 555-310-4821</li>
      <li>Fax: 555-310-4830</li>
      <li class="contact__web">rtautosales.biz</li>
    </ul>
  </section>

  <!-- Dark back -->
  <section class="card card--dark pos-br">
    <div class="vehicle-photo" role="img" aria-label="Dim photo of a pickup truck"></div>
    <div class="brand brand--back">RT Auto Sales</div>
  </section>

</main>
</body>
</html>
```